Wrenfield Acres Farm Postcard Design

I am looking for a new postcard design to mail out this season. We are a Farm business that does wholesale and retail and bulk seasoned firewood sales. we sell firewood from anything from bagged wood to tractor trailer loads of wood. We sell firewood in bulk bags. Pick up or delivery available there is no order to big or too small. I need my business name and phone number on the cards Wrenfield Acres Farm 848-613-0572 (call or text) I would like it to say we are the best priced guaranteed. I want something that is simple and straight forward but also really catches the eye when they see these in the mail box. I attached my logo and feel free to use photos of split firewood if you would like. id like my email on the card Wrenfieldacres90@mailbrook.net.

Target Market(s)

Firewood purchasers

Industry/Entity Type

agriculture

Requirements
Must have
• email phone number logo

```html
<!DOCTYPE html>
<html lang="en">
<head>
<meta charset="utf-8">
<title>Wrenfield Acres Farm Postcard</title>
<link rel="stylesheet" href="https://fonts.googleapis.com/css2?family=Oswald:wght@600;700&family=Montserrat:wght@500;700;800;900&display=swap">
<style>
  :root {
    --ink: #0b0b0b;
    --maroon: #6a0e12;
    --maroon-deep: #2b0608;
    --orange: #ec6a1f;
    --yellow: #f6c21b;
    --white: #ffffff;
    --text-dark: #151515;
    --badge-top: #f8a51c;
    --badge-bottom: #e61f4d;
  }
  * { box-sizing: border-box; margin: 0; padding: 0; }
  html, body { width: 1200px; height: 1200px; overflow: hidden; background: var(--white); }
  body { position: relative; font-family: "Montserrat", Arial, sans-serif; }

  .postcard {
    position: absolute; left: 216px; width: 774px; height: 518px; overflow: hidden;
    box-shadow: 0 2px 8px rgba(0,0,0,0.25);
  }
  .postcard--front {
    top: 62px;
    background: linear-gradient(90deg, var(--ink) 0 34%, var(--maroon-deep) 55%, var(--maroon) 100%);
  }
  .postcard--back { top: 624px; height: 516px; background: var(--white); }
  .abs { position: absolute; }

  /* front */
  .front-stripe { left: 0; top: 0; width: 774px; height: 300px; }
  .hero-photo {
    left: 300px; top: 40px; width: 440px; height: 250px;
    background: radial-gradient(ellipse at 45% 55%, #7a1218 0%, #3d0a0d 45%, rgba(30,6,8,0) 75%);
  }
  .brand {
    left: 24px; top: 40px; width: 240px;
    font-family: "Montserrat", Arial, sans-serif; font-weight: 900;
    font-size: 34px; line-height: 1.08; color: var(--orange); text-transform: uppercase;
  }
  .headline {
    left: 570px; top: 30px; z-index: 2;
    font-family: "Oswald", Impact, sans-serif; font-weight: 700;
    font-size: 31px; line-height: 37px; text-transform: uppercase;
  }
  .headline .white { color: var(--white); }
  .headline .yellow { color: var(--yellow); }
  .headline .orange { color: var(--orange); }

  .services-tab {
    left: 24px; top: 264px; width: 226px; height: 38px; background: var(--orange);
    clip-path: polygon(0 0, 88% 0, 100% 100%, 0 100%);
    font-weight: 900; font-style: italic; font-size: 25px; color: var(--ink);
    padding-left: 10px; line-height: 38px; letter-spacing: 0.5px;
  }
  .services-box {
    left: 24px; top: 300px; width: 726px; height: 133px;
    border: 3px solid var(--orange); background: var(--ink);
  }
  .services-text {
    left: 58px; top: 324px; font-weight: 800; font-size: 24px; line-height: 30px;
    color: var(--white); text-transform: uppercase; letter-spacing: 0.3px;
  }
  .firewood {
    background: radial-gradient(ellipse at 50% 55%, #e0a96b 0%, #b9773f 45%, rgba(150,90,40,0) 72%);
  }
  .firewood--front { left: 462px; top: 304px; width: 168px; height: 124px; }

  .badge { width: 112px; height: 112px; }
  .badge svg { position: absolute; inset: 0; width: 100%; height: 100%; }
  .badge-text {
    position: absolute; inset: 0; display: flex; flex-direction: column;
    align-items: center; justify-content: center; color: var(--white);
    font-weight: 900; text-transform: uppercase; line-height: 1;
  }
  .badge-text .big { font-size: 21px; }
  .badge-text .small { font-size: 9px; margin-top: 3px; font-weight: 800; }
  .badge--front { left: 626px; top: 311px; }
  .badge--back { left: 290px; top: 88px; z-index: 3; }

  /* contact bar */
  .contact-bar { left: 0; width: 774px; height: 62px; background: var(--orange); }
  .postcard--front .contact-bar { top: 456px; }
  .postcard--back .contact-bar { top: 454px; }
  .contact-email {
    position: absolute; left: 58px; top: 0; width: 410px; height: 100%; background: var(--white);
    clip-path: polygon(18px 0, 100% 0, calc(100% - 26px) 100%, 0 100%);
    font-weight: 700; font-size: 19px; color: var(--text-dark);
    line-height: 62px; padding-left: 36px;
  }
  .icon { position: absolute; width: 36px; height: 36px; top: 13px; }
  .icon--mail { left: 12px; }
  .icon--phone { left: 488px; }
  .contact-call {
    position: absolute; left: 532px; top: 6px; color: var(--white);
    font-weight: 800; text-transform: uppercase; line-height: 25px;
  }
  .contact-call .label { font-size: 22px; }
  .contact-call .number { font-size: 24px; }

  /* back */
  .back-panel { left: 0; top: 0; width: 774px; height: 454px; }
  .back-headline {
    left: 22px; top: 18px; font-weight: 800; font-size: 26px; line-height: 30px;
    color: var(--white); text-transform: uppercase;
  }
  .back-rule { left: 22px; top: 76px; width: 164px; height: 2px; background: var(--orange); }
  .back-sub {
    left: 22px; top: 89px; font-weight: 500; font-size: 17px; line-height: 19px;
    color: var(--white); text-transform: uppercase;
  }
  .equipment-photo {
    left: 19px; top: 151px; width: 317px; height: 293px;
    background: linear-gradient(180deg, #8fb2d6 0%, #6f8a6a 35%, #1f4a32 60%, #c9b27a 100%);
  }
  .firewood--back { left: 306px; top: 318px; width: 168px; height: 126px; }

  .indicia {
    left: 634px; top: 32px; width: 120px; height: 90px; border: 1px solid #333;
    text-align: center; font-family: Arial, Helvetica, sans-serif; font-weight: 700;
    font-size: 12.5px; line-height: 15px; padding-top: 7px; color: #000;
  }
  .indicia .paid { font-size: 15px; line-height: 18px; }
  .address-box {
    left: 512px; top: 167px; width: 187px; height: 66px; border: 1px solid #333;
    font-family: Arial, Helvetica, sans-serif; font-size: 15px; line-height: 18px;
    text-align: center; padding-top: 14px; color: #111;
  }
</style>
</head>
<body>

<svg width="0" height="0" style="position:absolute" aria-hidden="true">
  <defs>
    <linearGradient id="badge-fill" x1="0" y1="0" x2="0" y2="1">
      <stop offset="0" stop-color="#f8a51c"/>
      <stop offset="1" stop-color="#e61f4d"/>
    </linearGradient>
    <symbol id="starburst" viewBox="-56 -56 112 112">
      <polygon fill="url(#badge-fill)" points="54,0 44.1,8.8 49.9,20.7 37.4,25 38.2,38.2 25,37.4 20.7,49.9 8.8,44.1 0,54 -8.8,44.1 -20.7,49.9 -25,37.4 -38.2,38.2 -37.4,25 -49.9,20.7 -44.1,8.8 -54,0 -44.1,-8.8 -49.9,-20.7 -37.4,-25 -38.2,-38.2 -25,-37.4 -20.7,-49.9 -8.8,-44.1 0,-54 8.8,-44.1 20.7,-49.9 25,-37.4 38.2,-38.2 37.4,-25 49.9,-20.7 44.1,-8.8"/>
    </symbol>
    <symbol id="mail-icon" viewBox="0 0 36 36">
      <circle cx="18" cy="18" r="16" fill="none" stroke="#fff" stroke-width="2.2"/>
      <rect x="10" y="12" width="16" height="12" rx="1.5" fill="#fff"/>
      <polyline points="10.5,12.8 18,19 25.5,12.8" fill="none" stroke="#ec6a1f" stroke-width="1.8"/>
    </symbol>
    <symbol id="phone-icon" viewBox="0 0 36 36">
      <circle cx="18" cy="18" r="16" fill="none" stroke="#fff" stroke-width="2.2"/>
      <path d="M12.5 10.5 l3 -0.5 l2 4.5 l-2 1.6 c1 2.3 2.6 3.9 4.9 4.9 l1.6 -2 l4.5 2 l-0.5 3 c-0.3 1.2 -1.4 1.8 -2.6 1.6 c-6.2 -1 -11 -5.8 -12 -12 c-0.2 -1.2 0.4 -2.3 1.6 -2.6z" fill="#fff"/>
    </symbol>
  </defs>
</svg>

<!-- Front of card -->
<section class="postcard postcard--front">
  <svg class="abs front-stripe" viewBox="0 0 774 300" aria-hidden="true">
    <polygon points="268,0 290,0 340,240 318,240" fill="var(--orange)"/>
  </svg>
  <div class="abs hero-photo" role="img" aria-label="Photo of a red semi truck tractor with chrome stacks"></div>

  <div class="abs brand">Wrenfield Acres Farm</div>

  <div class="abs headline">
    <div class="white">Wholesale</div>
    <div class="white">and Retail</div>
    <div class="yellow">Bulk Seasoned</div>
    <div class="orange">Firewood Sales</div>
  </div>

  <div class="abs services-tab">★SERVICES★</div>
  <div class="abs services-box"></div>
  <p class="abs services-text">We sell firewood from<br>bagged wood to tractor<br>trailer loads of wood</p>
  <div class="abs firewood firewood--front" role="img" aria-label="Photo of a stack of split firewood"></div>

  <div class="abs badge badge--front">
    <svg aria-hidden="true"><use href="#starburst"/></svg>
    <div class="badge-text"><span class="big">Best</span><span class="big">Price</span><span class="small">Guaranteed</span></div>
  </div>

  <div class="abs contact-bar">
    <svg class="icon icon--mail" aria-hidden="true"><use href="#mail-icon"/></svg>
    <div class="contact-email">Wrenfieldacres90@mailbrook.net</div>
    <svg class="icon icon--phone" aria-hidden="true"><use href="#phone-icon"/></svg>
    <div class="contact-call"><div class="label">Call or Text</div><div class="number">848-613-0572</div></div>
  </div>
</section>

<!-- Back of card -->
<section class="postcard postcard--back">
  <svg class="abs back-panel" viewBox="0 0 774 454" aria-hidden="true">
    <polygon points="0,0 414,0 474,454 0,454" fill="var(--ink)"/>
    <polygon points="0,0 398,0 380,142 0,142" fill="var(--maroon)"/>
  </svg>

  <h2 class="abs back-headline">Pick up or delivery<br>available</h2>
  <div class="abs back-rule"></div>
  <p class="abs back-sub">There is no order<br>to big or too small</p>

  <div class="abs badge badge--back">
    <svg aria-hidden="true"><use href="#starburst"/></svg>
    <div class="badge-text"><span class="big">Best</span><span class="big">Price</span><span class="small">Guaranteed</span></div>
  </div>

  <div class="abs equipment-photo" role="img" aria-label="Photo of a green and yellow firewood processor in a wooded yard"></div>
  <div class="abs firewood firewood--back" role="img" aria-label="Photo of a stack of split firewood"></div>

  <div class="abs indicia">PRSRT STD<br>ECRWSS<br>U.S.POSTAGE<br><span class="paid">PAID</span><br>EDDM Retail</div>
  <div class="abs address-box">Local Postal<br>Customer</div>

  <div class="abs contact-bar">
    <svg class="icon icon--mail" aria-hidden="true"><use href="#mail-icon"/></svg>
    <div class="contact-email">Wrenfieldacres90@mailbrook.net</div>
    <svg class="icon icon--phone" aria-hidden="true"><use href="#phone-icon"/></svg>
    <div class="contact-call"><div class="label">Call or Text</div><div class="number">848-613-0572</div></div>
  </div>
</section>

</body>
</html>
```